ultra-minimalist business card

front (black background, matte):

tarik b. hosseny
writer | photographer
get@tarikhosseny.com

back (white background, matte):

a picture speaks a thousand words;
a word draws a thousand pictures.

www.tarikhosseny.com

all text should be small (white or silver - as long as it shows against the black - on the front; black or gray - as long as it shows against the white - on the back).

feel free to get creative in terms of arrangement, alignment, and font type, but remember, the overall style is minimalist, so nothing too fancy, please.

thanks.

```html
<!DOCTYPE html>
<html lang="en">
<head>
<meta charset="utf-8">
<title>Tarik b. Hosseny — Business Card</title>
<link rel="stylesheet" href="https://fonts.googleapis.com/css2?family=Zilla+Slab:wght@300;400;500&family=Lato:wght@300&display=swap">
<style>
  :root {
    --backdrop: #d9d9d7;
    --card-black: #1d1d1d;
    --card-white: #efeeea;
    --ink-light: #ecebe8;
    --ink-silver: #8f8f8f;
    --ink-dark: #1a1a1a;
    --edge-shadow: rgba(0, 0, 0, 0.18);
  }

  * { box-sizing: border-box; margin: 0; padding: 0; }

  html, body {
    width: 1200px;
    height: 900px;
    overflow: hidden;
    background: var(--backdrop);
  }

  .canvas {
    position: relative;
    width: 1200px;
    height: 900px;
    display: flex;
    flex-direction: column;
    align-items: center;
    justify-content: center;
    gap: 56px;
  }

  .card {
    position: relative;
    width: 660px;
    height: 377px;
    box-shadow: 0 2px 6px var(--edge-shadow);
  }

  /* Back side: white card with quote and web address */
  .card--back {
    background: var(--card-white);
    color: var(--ink-dark);
    font-family: "Zilla Slab", serif;
    text-align: center;
  }

  .quote {
    position: absolute;
    top: 118px;
    left: 0;
    right: 0;
    line-height: 1.45;
  }

  .quote__line {
    display: block;
    font-weight: 400;
    font-size: 19px;
    letter-spacing: 0.2px;
  }

  .quote__line--second {
    font-size: 17px;
  }

  .web-address {
    position: absolute;
    top: 268px;
    left: 0;
    right: 0;
    font-weight: 500;
    font-size: 16px;
    letter-spacing: 0.8px;
  }

  /* Front side: black card with identity and email */
  .card--front {
    background: var(--card-black);
  }

  .identity {
    position: absolute;
    left: 56px;
    bottom: 58px;
    display: flex;
    align-items: flex-end;
  }

  .identity__name-block {
    padding-right: 14px;
  }

  .identity__name {
    font-family: "Zilla Slab", serif;
    font-weight: 300;
    font-size: 30px;
    line-height: 1;
    color: var(--ink-light);
    letter-spacing: 0.3px;
  }

  .identity__role {
    margin-top: 6px;
    font-family: "Lato", sans-serif;
    font-weight: 300;
    font-size: 14px;
    color: var(--ink-silver);
    letter-spacing: 0.3px;
  }

  .identity__divider {
    width: 1px;
    height: 46px;
    background: var(--ink-light);
    opacity: 0.85;
  }

  .identity__email {
    padding-left: 12px;
    font-family: "Zilla Slab", serif;
    font-weight: 300;
    font-size: 18px;
    color: var(--ink-light);
    letter-spacing: 0.3px;
    line-height: 1;
    padding-bottom: 2px;
  }
</style>
</head>
<body>
  <main class="canvas">
    <section class="card card--back" aria-label="Card back">
      <p class="quote">
        <span class="quote__line">A picture speaks a thousand words</span>
        <span class="quote__line quote__line--second">A word draws a thousand pictures</span>
      </p>
      <p class="web-address">www.tarikhosseny.com</p>
    </section>

    <section class="card card--front" aria-label="Card front">
      <div class="identity">
        <div class="identity__name-block">
          <h1 class="identity__name">Tarik b. hosseny</h1>
          <p class="identity__role">Writer | Photographer</p>
        </div>
        <span class="identity__divider" aria-hidden="true"></span>
        <p class="identity__email">get@tarikhosseny.com</p>
      </div>
    </section>
  </main>
</body>
</html>
```